Letterhead & Business Card for our Professional Practice (Financial Services)

We are looking for someone to design a letterhead and business card for our business, which is a professional practice called Harbor Lumen Capital Limited. The website is at www.harborrlumencapital.example.co.uk.

The letterhead needs to have: (a) our logo (b) address (c) telephone number (d) email address and (e) our company number.

We would like the stationary to be consistent with the website.

I have attached the logo in EPS and PNG format.

Target Market(s)

Professional services, large commercial enterprises, financial services

Industry/Entity Type

Financial Service

Font styles to use
Serif

Colors
3176b5
f04a50

Requirements
Must have
• Be consistent with our website located at www.harborlumencapital.example.co.uk
• Be in the following formats:
• 1. Word template for the letterhead
• 2. PDF for the letterhead with setup and bleeds required at www.presskite.example.co.uk
• 3. PDF for the business card with setup and bleeds required at www.presskite.example.co.uk
Nice to have
• Something with a really interesting design that says "these guys are professional but dynamic and interesting"
Should not have
• Boring

```html
<!DOCTYPE html>
<html lang="en">
<head>
<meta charset="utf-8">
<title>Harbor Lumen Capital – Business Card</title>
<link rel="stylesheet" href="https://fonts.googleapis.com/css2?family=Open+Sans:wght@400;600;700&display=swap">
<style>
  :root {
    --page: #e4dfd8;
    --card: #f0f0f0;
    --card-shade: #e6e6e6;
    --slate-blue: #4f7a9a;
    --rose-red: #d05a6e;
    --navy: #1c3f8a;
    --brand-red: #d8283a;
    --ink: #2a2a2a;
    --icon-grey: #a9a9a9;
  }
  * { box-sizing: border-box; margin: 0; padding: 0; }
  html, body { width: 1200px; height: 746px; overflow: hidden; }
  body {
    background: var(--page);
    font-family: "Open Sans", Arial, sans-serif;
    display: flex;
    align-items: center;
    justify-content: center;
    gap: 40px;
  }
  .card {
    position: relative;
    width: 540px;
    height: 310px;
    background: var(--card);
    overflow: hidden;
    box-shadow: 0 10px 24px rgba(60, 40, 20, 0.22);
  }
  .card__texture {
    position: absolute;
    inset: 0;
    background:
      radial-gradient(circle at 30% 70%, var(--card-shade), transparent 60%),
      radial-gradient(circle at 75% 30%, var(--card-shade), transparent 55%),
      var(--card);
  }
  .corner { position: absolute; }
  .corner--top { top: 0; left: 0; }
  .corner--bottom { bottom: 0; right: 0; }

  .brand {
    position: absolute;
    display: flex;
    align-items: center;
    gap: 10px;
  }
  .brand__mark { background: var(--brand-red); flex: none; }
  .brand__name {
    color: var(--navy);
    font-weight: 700;
    white-space: nowrap;
  }

  /* front */
  .card--front .brand { left: 112px; top: 118px; }
  .card--front .brand__mark { width: 44px; height: 44px; }
  .card--front .brand__name { font-size: 30px; letter-spacing: 0.3px; }
  .card__url {
    position: absolute;
    left: 168px;
    top: 172px;
    font-size: 12.5px;
    font-weight: 600;
    color: var(--ink);
  }

  /* back */
  .card--back .brand { left: 22px; top: 150px; }
  .card--back .brand__mark { width: 20px; height: 20px; }
  .card--back .brand__name { font-size: 15px; }
  .contact {
    position: absolute;
    left: 240px;
    top: 56px;
    list-style: none;
    font-size: 11px;
    line-height: 1.4;
    color: var(--ink);
  }
  .contact__row {
    display: flex;
    gap: 9px;
    margin-bottom: 11px;
    white-space: nowrap;
  }
  .contact__icon { flex: none; width: 17px; height: 17px; margin-top: 1px; }
  .contact__name { font-weight: 600; }
</style>
</head>
<body>

  <section class="card card--back" aria-label="Business card, details side">
    <div class="card__texture" role="img" aria-label="Subtle light grey hexagon background pattern"></div>
    <svg class="corner corner--top" width="230" height="120" viewBox="0 0 230 120">
      <path d="M0 0 H170 Q215 0 220 45 Q224 112 160 112 H0 Z" fill="var(--slate-blue)"/>
    </svg>
    <svg class="corner corner--bottom" width="180" height="100" viewBox="0 0 180 100">
      <path d="M180 0 V100 H36 Q0 100 4 66 Q10 20 62 16 Z" fill="var(--rose-red)"/>
    </svg>

    <div class="brand">
      <span class="brand__mark"></span>
      <span class="brand__name">Harbor Lumen Capital</span>
    </div>

    <ul class="contact">
      <li class="contact__row">
        <svg class="contact__icon" viewBox="0 0 18 18"><polygon points="9,0 17,4.5 17,13.5 9,18 1,13.5 1,4.5" fill="var(--icon-grey)"/><circle cx="9" cy="7" r="2.5" fill="#fff"/><path d="M4.8 13 Q9 8.8 13.2 13 Z" fill="#fff"/></svg>
        <div><div class="contact__name">Mr. Name Surname</div><div>Designation</div><div>+11 1234567891</div></div>
      </li>
      <li class="contact__row">
        <svg class="contact__icon" viewBox="0 0 18 18"><polygon points="9,0 17,4.5 17,13.5 9,18 1,13.5 1,4.5" fill="var(--icon-grey)"/><path d="M9 4 A3 3 0 0 1 12 7 Q12 9 9 13 Q6 9 6 7 A3 3 0 0 1 9 4 Z" fill="#fff"/><circle cx="9" cy="7" r="1" fill="var(--icon-grey)"/></svg>
        <div>14-16 Quayside Row, Eastbrook,<br>Fenshire, EB2 4QN</div>
      </li>
      <li class="contact__row">
        <svg class="contact__icon" viewBox="0 0 18 18"><polygon points="9,0 17,4.5 17,13.5 9,18 1,13.5 1,4.5" fill="var(--icon-grey)"/><path d="M6 5 L7.5 5 L8.3 7.2 L7.3 8 Q8 9.8 10 10.7 L10.8 9.7 L13 10.5 L13 12 Q12.5 13 11.5 13 Q6.8 12.5 5 6.5 Q5 5.5 6 5 Z" fill="#fff"/></svg>
        <div>01632 960418</div>
      </li>
      <li class="contact__row">
        <svg class="contact__icon" viewBox="0 0 18 18"><polygon points="9,0 17,4.5 17,13.5 9,18 1,13.5 1,4.5" fill="var(--icon-grey)"/><rect x="4.5" y="6" width="9" height="6.5" fill="#fff"/><path d="M4.5 6 L9 9.6 L13.5 6" fill="none" stroke="var(--icon-grey)" stroke-width="0.9"/></svg>
        <div>contact@harborlumencapital.example.co.uk</div>
      </li>
    </ul>
  </section>

  <section class="card card--front" aria-label="Business card, brand side">
    <div class="card__texture" role="img" aria-label="Subtle light grey hexagon background pattern"></div>
    <svg class="corner corner--top" width="240" height="120" viewBox="0 0 240 120">
      <path d="M0 0 H185 Q228 0 232 42 Q236 110 170 110 H0 Z" fill="var(--slate-blue)"/>
    </svg>
    <svg class="corner corner--bottom" width="200" height="125" viewBox="0 0 200 125">
      <path d="M200 0 V125 H42 Q0 125 4 82 Q10 26 70 20 Z" fill="var(--rose-red)"/>
    </svg>

    <div class="brand">
      <span class="brand__mark"></span>
      <span class="brand__name">Harbor Lumen Capital</span>
    </div>
    <p class="card__url">www.harborlumencapital.example.co.uk</p>
  </section>

</body>
</html>
```